Korvanta

1. We need a four color business card
2. The Front of card needs to include our Logo, Slogan which is "Launching, Expanding & Optimizing Organizations, Individual Name, email, two phone numbers, email, skype address, website address
3. Back of card needs to include the following topics: Start Ups & Business Optimization,Product Acquisition, Destination Product Marketing & Representation,Marketing & Sales, Operations, Training/Education, Digital Marketing, Keynote Addresses/Public Speaking
3. Back of card can not be black as it needs to be a color that people can write on
Industry/Entity Type
Business

```html
<!DOCTYPE html>
<html lang="en">
<head>
<meta charset="utf-8">
<title>Korvanta Business Card</title>
<link rel="stylesheet" href="https://fonts.googleapis.com/css2?family=Arimo:wght@400;700&display=swap">
<style>
:root{
  --page:#e9e7e3;
  --card-front:#ffffff;
  --card-back-top:#f1f1f1;
  --card-back-bottom:#c9c9c9;
  --blue:#1f5ea8;
  --green:#8cbf3f;
  --orange:#f39325;
  --ink:#555a5f;
  --rule:#9a9a9a;
  --icon:#2b5f9e;
}
*{margin:0;padding:0;box-sizing:border-box}
html,body{width:1200px;height:784px;overflow:hidden}
body{background:var(--page);font-family:"Arimo",Arial,sans-serif;position:relative}
.card{position:absolute;top:225px;width:550px;height:334px;border-radius:4px;box-shadow:0 6px 18px rgba(0,0,0,.18);overflow:hidden}
.card-back{left:30px;background:linear-gradient(160deg,var(--card-back-top),var(--card-back-bottom));
  display:flex;flex-direction:column;align-items:center;justify-content:center;gap:9px}
.service{font-variant:small-caps;font-weight:700;letter-spacing:2.5px;font-size:17px;text-align:center}
.service.blue{color:var(--blue)}
.service.green{color:var(--green)}
.service.orange{color:var(--orange)}
.card-front{left:620px;background:var(--card-front);padding:26px 36px 24px}
.brand{display:flex;align-items:center;gap:12px}
.brand-dot{width:48px;height:48px;border-radius:50%;background:var(--blue);flex:none}
.brand-name{font-size:42px;line-height:48px;font-weight:700;color:var(--blue);letter-spacing:.5px}
.slogan{margin:6px 0 0 60px;padding-top:5px;border-top:1px solid var(--rule);width:300px;
  font-variant:small-caps;font-size:12px;line-height:14px;letter-spacing:1.2px;color:var(--ink)}
.person{margin-top:24px}
.person-name{font-size:22px;line-height:26px;font-weight:700;color:var(--blue)}
.person-title{font-size:15px;line-height:18px;color:var(--ink);margin-top:2px}
.contacts{list-style:none;margin-top:8px}
.contacts li{display:flex;align-items:center;gap:8px;font-size:16px;color:var(--ink);line-height:22px}
.contacts svg{width:16px;height:16px;flex:none}
</style>
</head>
<body>
<section class="card card-back" aria-label="Card back: services">
  <p class="service blue">Start Ups &amp; Business Optimization</p>
  <p class="service green">Product Acquisition</p>
  <p class="service orange">Destination Product Marketing &amp; Representation</p>
  <p class="service blue">Marketing &amp; Sales</p>
  <p class="service green">Operations</p>
  <p class="service orange">Training/Education</p>
  <p class="service blue">Digital Marketing</p>
  <p class="service green">Keynote Addresses/Public Speaking</p>
</section>

<section class="card card-front" aria-label="Card front">
  <div class="brand">
    <span class="brand-dot"></span>
    <span class="brand-name">Korvanta</span>
  </div>
  <p class="slogan">Launching, Expanding &amp; Optimizing Organizations</p>
  <div class="person">
    <p class="person-name">Mara Quill</p>
    <p class="person-title">President</p>
  </div>
  <ul class="contacts">
    <li><svg viewBox="0 0 16 16"><path d="M3 1h3l1 4-2 1a9 9 0 0 0 5 5l1-2 4 1v3a2 2 0 0 1-2 2C7 15 1 9 1 3a2 2 0 0 1 2-2z" fill="var(--icon)"/></svg>(555)210-4836</li>
    <li><svg viewBox="0 0 16 16"><path d="M3 1h3l1 4-2 1a9 9 0 0 0 5 5l1-2 4 1v3a2 2 0 0 1-2 2C7 15 1 9 1 3a2 2 0 0 1 2-2z" fill="var(--icon)"/></svg>(555)210-4972</li>
    <li><svg viewBox="0 0 16 16"><rect x="1" y="3" width="14" height="10" rx="1" fill="var(--icon)"/><path d="M1.5 4l6.5 5 6.5-5" stroke="#fff" stroke-width="1.3" fill="none"/></svg>mara@korvanta.com</li>
    <li><svg viewBox="0 0 16 16"><circle cx="8" cy="8" r="7" fill="var(--icon)"/><g stroke="#fff" stroke-width="1" fill="none"><ellipse cx="8" cy="8" rx="3" ry="7"/><path d="M1 8h14M2.5 4.5h11M2.5 11.5h11"/></g></svg>www.korvanta</li>
    <li><svg viewBox="0 0 16 16"><circle cx="8" cy="8" r="7" fill="var(--icon)"/></svg>mara_korvanta</li>
  </ul>
</section>
</body>
</html>
```